A 'new law' boutique Australian law firm that provides specialist employment law and people managem

We value helping clients create results with respect workplaces. What differentiates us is we provide actionable training in understanding and dealing with people and ensure legal compliance fits with this approach. We would like a fresh approach to our training overview documents that we currently use in our current law firm (6 attached). Please use pictures, symbols etc consistent with our non-traditional law approach that captures the approach of each training session.. Attached is the logo and draft letterhead for Brook Legal which will launch soon.

Target Market(s)

HR Managers and in-house lawyers (non employment specialists) in mid-large Australian companies that are progressive with a relationship based approach to managing employee behaviours and disputes.

Industry/Entity Type

Human Resource

Font styles to use
Sans Serif

Colors
3176b5
33a6d7

Requirements
Must have
• 1 or 2 page PDF for each of the 6 documents that the wording supplied goes into your design which will be pretty similar as we want consistency with our documents

```html
<!DOCTYPE html>
<html lang="en">
<head>
<meta charset="utf-8">
<title>Contact Officer Training – Brook Legal</title>
<link rel="stylesheet" href="https://fonts.googleapis.com/css2?family=Oswald:wght@400;500;600;700&family=Lato:wght@400;700&family=Montserrat:wght@600;700&display=swap">
<style>
  :root{
    --brand-blue:#3176b5;
    --bright-blue:#33a6d7;
    --panel-blue:#1e72c4;
    --ink:#2f2f2f;
    --slate:#555759;
    --charcoal:#3f4042;
    --soft-grey:#f2f2f2;
    --rule:#c9c9c9;
    --backdrop:#8a8d90;
    --white:#ffffff;
  }
  *{box-sizing:border-box;margin:0;padding:0}
  html,body{width:1200px;height:1200px;overflow:hidden}
  body{background:var(--backdrop);font-family:"Lato",sans-serif;color:var(--ink)}
  .flyer{position:absolute;left:175px;top:0;width:850px;height:1200px;background:var(--white);overflow:hidden}
  .abs{position:absolute}

  /* Header */
  .masthead{left:0;top:0;width:850px;height:208px;
    background:linear-gradient(100deg,#1a5fb8 0%,#2a82d6 45%,#5aa8e8 70%,#2a7fd3 100%)}
  .masthead-title{left:47px;top:34px;font-family:"Oswald",sans-serif;font-weight:600;color:var(--white);line-height:1}
  .masthead-title .line-small{display:block;font-size:54px;letter-spacing:-0.5px}
  .masthead-title .line-big{display:block;font-size:86px;font-weight:700;margin-top:4px;letter-spacing:-1px}
  .brand{left:628px;top:84px;display:flex;align-items:center;gap:10px;
    font-family:"Lato",sans-serif;font-weight:700;font-size:26px;color:var(--white);line-height:1}
  .brand-dot{width:18px;height:18px;border-radius:50%;background:var(--white);flex:none}

  /* Training need */
  .need-icon{left:57px;top:230px;width:68px;height:78px;border-radius:6px;background:var(--panel-blue);opacity:.9}
  .need-heading{left:35px;top:323px;width:130px;text-align:center;font-family:"Oswald",sans-serif;font-weight:700;line-height:1}
  .need-heading .word-blue{display:block;font-size:32px;color:var(--brand-blue)}
  .need-heading .word-grey{display:block;font-size:40px;color:#6d6e70;margin-top:2px}
  .need-copy{font-size:12.4px;line-height:19.5px;color:var(--ink);text-align:justify}
  .need-copy p + p{margin-top:19px}
  .need-a{left:183px;top:230px;width:333px}
  .need-b{left:535px;top:230px;width:286px}

  /* Overview */
  .overview-band{left:0;top:424px;width:850px;height:42px;background:#5a5b5d;color:var(--white);
    font-family:"Montserrat",sans-serif;font-weight:600;font-size:21px;letter-spacing:1px;
    display:flex;align-items:center;justify-content:center}
  .overview-body{left:0;top:466px;width:850px;height:376px;background:var(--soft-grey)}
  .col-rule{top:480px;width:1px;height:350px;background:var(--rule)}
  .topic{width:234px}
  .topic-head{display:flex;align-items:center;gap:9px;font-family:"Oswald",sans-serif;font-weight:500;font-size:15px;color:var(--ink);height:28px}
  .topic-icon{width:26px;height:26px;border-radius:5px;background:var(--panel-blue);flex:none}
  .topic-doc{flex:none}
  .topic-text{margin-top:6px;font-size:11.6px;line-height:15px;text-align:justify;color:var(--ink)}
  .topic-text.plain{text-align:left}

  /* Learning outcomes */
  .outcomes-band{left:0;top:852px;width:360px;height:40px;background:#58595b;color:var(--white);
    font-family:"Montserrat",sans-serif;font-weight:700;font-size:21px;letter-spacing:0.8px;padding-left:34px;
    display:flex;align-items:center}
  .outcomes-panel{left:0;top:894px;width:360px;height:306px;background:var(--panel-blue);color:var(--white);padding:18px 12px 0 32px}
  .outcomes-intro{font-weight:700;font-size:13.6px;line-height:16.5px}
  .outcomes-list{list-style:none;margin-top:12px}
  .outcomes-list li{display:flex;gap:7px;font-size:12.6px;line-height:15.5px;margin-bottom:7.5px}
  .outcomes-list .num{flex:none;width:16px;height:16px;border-radius:50%;background:var(--white);color:var(--panel-blue);
    font-size:10px;font-weight:700;display:flex;align-items:center;justify-content:center}
  .team-photo{left:363px;top:852px;width:487px;height:263px;
    background:linear-gradient(180deg,#e9eef2 0%,#c9d3dc 45%,#b88a6c 75%,#8d6a55 100%)}
  .contact-bar{left:363px;top:1115px;width:487px;height:85px;background:var(--charcoal);color:var(--white);
    font-size:12.2px;padding:17px 0 0 28px}
  .contact-row{display:flex;align-items:center;gap:8px;height:22px}
  .contact-row + .contact-row{margin-top:6px}
  .contact-item{display:flex;align-items:center;gap:8px;margin-right:6px}
  .badge{width:20px;height:20px;border-radius:50%;background:var(--white);display:flex;align-items:center;justify-content:center;flex:none}
  .badge-blank{width:20px;height:20px;border-radius:50%;background:var(--white);flex:none}
</style>
</head>
<body>
<main class="flyer">

  <header class="abs masthead" role="img" aria-label="Blue-toned photo of hands working on a laptop"></header>
  <h1 class="abs masthead-title"><span class="line-small">CONTACT OFFICER</span><span class="line-big">TRAINING</span></h1>
  <div class="abs brand"><span class="brand-dot"></span>Brook Legal</div>

  <section>
    <div class="abs need-icon" role="img" aria-label="Icon of a trainer at a flip chart with an audience"></div>
    <h2 class="abs need-heading"><span class="word-blue">TRAINING</span><span class="word-grey">NEED</span></h2>
    <div class="abs need-copy need-a">
      <p>Unlawful or inappropriate behavior in the workplace that is left unaddressed can impact on productivity and employee retention. Claims can be costly in terms of time and money as well as the impact on mental health from being involved in uncomfortable adversarial processes.</p>
      <p>Clear policies and procedures explaining the organisation’s workplace behavior expectations and how grievances will be managed are a minimum compliance requirement.</p>
    </div>
    <div class="abs need-copy need-b">
      <p>The challenge is ensuring that employees understand the directions contained in those policies, what is unlawful and inappropriate behaviour and the options available to address those behaviours if they experience them or engage in them.</p>
      <p>Well trained Contact Officers provide another resource to assist the organisation to provide a safe and respectful workplace</p>
    </div>
  </section>

  <h2 class="abs overview-band">OVERVIEW OF TRANING</h2>
  <section class="abs overview-body"></section>
  <div class="abs col-rule" style="left:290px"></div>
  <div class="abs col-rule" style="left:566px"></div>

  <div class="abs topic" style="left:41px;top:490px">
    <h3 class="topic-head"><span class="topic-icon" role="img" aria-label="Discrimination icon"></span>Discrimination</h3>
    <p class="topic-text">What is direct and indirect discrimination? What are the prescribed attributes? What are the exceptions to the general rules. Practical examples of behaviour that may be discriminatory.</p>
  </div>
  <div class="abs topic" style="left:41px;top:611px">
    <h3 class="topic-head"><span class="topic-icon" role="img" aria-label="Bullying icon"></span>Bullying</h3>
    <p class="topic-text">What is bullying. Explore how bullying differs to discrimination or inappropriate behaviour. Performance Management - when it will and will not be bullying. Is all workplace conflict bullying? Practical examples of behaviour that may be bullying.</p>
  </div>
  <div class="abs topic" style="left:38px;top:754px">
    <h3 class="topic-head"><span class="topic-icon" role="img" aria-label="Test learning icon"></span>Test Learning</h3>
    <p class="topic-text plain">Role play, group discussion</p>
  </div>

  <div class="abs topic" style="left:314px;top:493px">
    <h3 class="topic-head"><span class="topic-icon" role="img" aria-label="Harassment icon"></span>Harassment</h3>
    <p class="topic-text">What is harassment? Are protected attributes relevant to harassment? What is the difference between harassment and sexual harassment? How does the reasonable person test work in relation to harassment? Practical examples of behaviour that may be harassment or sexual harassment.</p>
  </div>
  <div class="abs topic" style="left:314px;top:652px">
    <h3 class="topic-head"><span class="topic-icon" role="img" aria-label="Victimisation icon"></span>Victimisation and Vilification</h3>
    <p class="topic-text plain">What is victimisation? What is Vilification?</p>
  </div>
  <div class="abs topic" style="left:314px;top:718px">
    <h3 class="topic-head"><span class="topic-icon" role="img" aria-label="Contact officer icon"></span>The Contact Officer’s role</h3>
    <p class="topic-text">How to perform your role when approached by an employee – the 6 step approach. What not to do. What are the obligations with regard to Confidentiality?</p>
  </div>

  <div class="abs topic" style="left:588px;top:496px">
    <h3 class="topic-head">
      <svg class="topic-doc" width="24" height="28" viewBox="0 0 24 28"><path d="M2 1h14l6 6v20H2z" fill="none" stroke="#1e72c4" stroke-width="2"/><path d="M6 12h12M6 16h12M6 20h12" stroke="#1e72c4" stroke-width="1.6"/></svg>
      Adverse Action</h3>
    <p class="topic-text">What is adverse action and how does it differ to other unlawful behaviour? What is a workplace right? When is it lawful to terminate employment because of an employee’s absence? How are the protected attributes relevant to adverse action?</p>
  </div>
  <div class="abs topic" style="left:588px;top:639px">
    <h3 class="topic-head">
      <svg class="topic-doc" width="26" height="28" viewBox="0 0 26 28"><rect x="1" y="1" width="4" height="26" fill="#1e72c4"/><rect x="8" y="3" width="17" height="24" fill="none" stroke="#1e72c4" stroke-width="2"/><path d="M11 9h11M11 13h11M11 17h11M11 21h11" stroke="#1e72c4" stroke-width="1.6"/></svg>
      Grievance Options</h3>
    <p class="topic-text">Explore the options of complaint management - self management, internal informal management, formal internal management. How do they compare and what are the advantages and disadvantages of each approach. Is doing nothing an option? External options – advantages and disadvantages. Who decides which option?</p>
  </div>

  <h2 class="abs outcomes-band">LEARNING OUTCOMES</h2>
  <section class="abs outcomes-panel">
    <p class="outcomes-intro">Training will enable participants to perform their role of Contact Officer and to understand</p>
    <ol class="outcomes-list">
      <li><span class="num">1</span>The role and responsibilities of a Contact Officer</li>
      <li><span class="num">2</span>What amounts to unlawful workplace behaviour</li>
      <li><span class="num">3</span>What is considered inappropriate behaviour in our workplace</li>
      <li><span class="num">4</span>How to apply understanding unlawful/inappropriate behaviour to common scenarios</li>
      <li><span class="num">5</span>How to address and resolve grievances early</li>
      <li><span class="num">6</span>Options to resolve grievances internally and the Contact Officer role</li>
      <li><span class="num">7</span>External options and their pros and cons for resolving grievances</li>
    </ol>
  </section>

  <div class="abs team-photo" role="img" aria-label="Photo of a smiling team gathered around a laptop in a bright office"></div>

  <footer class="abs contact-bar">
    <div class="contact-row">
      <span class="badge"><svg width="12" height="14" viewBox="0 0 12 14"><path d="M6 13C2 8 1 6.5 1 5a5 5 0 0110 0c0 1.5-1 3-5 8z" fill="#1e72c4"/><circle cx="6" cy="5" r="1.8" fill="#fff"/></svg></span>
      18 Harbour Rd, Sandy Bay and Level 4, 210 Flinders Ln, Melbourne
    </div>
    <div class="contact-row">
      <span class="contact-item"><span class="badge"><svg width="12" height="12" viewBox="0 0 12 12"><path d="M2.5 1l2 2.5-1.2 1.3a7 7 0 003.9 3.9L8.5 7.5 11 9.5 9.8 11C5 10.6 1.4 7 1 2.2z" fill="#1e72c4"/></svg></span>1300 55 0192</span>
      <span class="contact-item"><span class="badge"><svg width="12" height="10" viewBox="0 0 12 10"><rect x="0.8" y="0.8" width="10.4" height="8.4" fill="none" stroke="#1e72c4" stroke-width="1.4"/><path d="M1 1l5 4.5L11 1" fill="none" stroke="#1e72c4" stroke-width="1.4"/></svg></span>hello@brooklegal.com.au</span>
      <span class="contact-item"><span class="badge-blank"></span>brooklegal</span>
    </div>
  </footer>

</main>
</body>
</html>
```